Open House Postcard

We need a postcard design for an Open House for our newly expanded showroom in Pittsford, NY featuring all the newest trends and products. We design and sell both Kitchen and Bath cabinetry and countertops. We are focusing this particular mailing to industry professional (remodelers, new home builders and interior designers). The Open House will be held Wednesday, November 12th from 8:30am - 6:00pm. At 6:00 we will be drawing one winner of a $500 Brantlys Gift Card! All attendees will receive a voucher for 10% off their first order with us (new customers only). The final design should include our website www.CabinetsByHollowell.com.

```html
<!DOCTYPE html>
<html lang="en">
<head>
<meta charset="utf-8">
<title>Open House Postcard – Cabinets by Hollowell</title>
<link rel="stylesheet" href="https://fonts.googleapis.com/css2?family=Pinyon+Script&family=Roboto+Slab:wght@800&family=Libre+Baskerville:wght@400;700&family=Arimo&display=swap">
<style>
  :root {
    --backdrop: #c6c7c9;
    --card: #ffffff;
    --slate: #4e7591;
    --brick: #7a3a22;
    --white: #ffffff;
    --photo-dark: #2a1d14;
    --photo-warm: #6b5340;
    --photo-light: #b9a88e;
  }
  * { margin: 0; padding: 0; box-sizing: border-box; }
  html, body { width: 1200px; height: 962px; overflow: hidden; }
  body { background: var(--backdrop); position: relative; font-family: "Libre Baskerville", Georgia, serif; }

  .postcard { position: absolute; left: 82px; top: 83px; width: 1036px; height: 795px; background: var(--card); }

  .invite-panel { position: absolute; left: 0; top: 0; width: 396px; height: 623px; background: var(--slate); color: var(--white); text-align: center; }
  .invite-lead { position: absolute; top: 26px; width: 100%; font-family: "Pinyon Script", cursive; font-size: 31px; }
  .rule { position: absolute; background: var(--white); }
  .rule-top { left: 49px; width: 289px; top: 82px; height: 6px; }
  .rule-bottom { left: 49px; width: 289px; top: 224px; height: 14px; }
  .headline { position: absolute; top: 94px; width: 100%; font-family: "Roboto Slab", serif; font-weight: 800; font-size: 66px; line-height: 60px; letter-spacing: 0.5px; }

  .label-row { position: absolute; left: 54px; width: 300px; height: 32px; display: flex; align-items: center; justify-content: space-between; }
  .label-row .lines { width: 94px; height: 14px; border-top: 4px solid var(--white); border-bottom: 4px solid var(--white); }
  .label-row .label { font-family: "Pinyon Script", cursive; font-size: 28px; }
  .label-when { top: 254px; }
  .label-where { top: 410px; }

  .event-day { position: absolute; top: 300px; width: 100%; font-weight: 700; font-size: 30px; }
  .event-date { position: absolute; top: 342px; width: 100%; font-weight: 700; font-size: 19px; }
  .event-time { position: absolute; top: 372px; width: 100%; font-weight: 700; font-size: 20px; }
  .event-address { position: absolute; top: 444px; width: 100%; font-weight: 700; font-size: 19.5px; line-height: 29px; }

  .marker { position: absolute; width: 74px; height: 74px; border-radius: 50%; background: var(--white); }
  .marker-left { left: 279px; top: 516px; }
  .marker-right { left: 474px; top: 516px; }

  .showroom-photo { position: absolute; left: 431px; top: 0; width: 605px; height: 623px;
    background: linear-gradient(160deg, var(--photo-warm) 0%, var(--photo-light) 35%, var(--photo-warm) 60%, var(--photo-dark) 100%); }

  .brand { position: absolute; left: 90px; top: 690px; width: 300px; display: flex; align-items: center; justify-content: center; gap: 12px; color: var(--brick); font-size: 27px; }
  .brand-mark { width: 22px; height: 22px; background: var(--slate); }

  .contact { position: absolute; left: 440px; top: 640px; width: 566px; text-align: center; }
  .contact-lead { font-family: "Pinyon Script", cursive; font-size: 31px; color: var(--slate); }
  .contact-web { margin-top: 8px; font-weight: 700; font-size: 20px; color: var(--brick); }
  .contact-phone { margin-top: 4px; font-family: "Arimo", Arial, sans-serif; font-size: 30px; color: var(--brick); }
</style>
</head>
<body>
  <main class="postcard">
    <section class="invite-panel">
      <p class="invite-lead">Please join us for an</p>
      <div class="rule rule-top"></div>
      <h1 class="headline">OPEN<br>HOUSE</h1>
      <div class="rule rule-bottom"></div>

      <div class="label-row label-when"><span class="lines"></span><span class="label">When?</span><span class="lines"></span></div>
      <p class="event-day">WEDNESDAY,</p>
      <p class="event-date">NOVEMBER 12</p>
      <p class="event-time">from 8:30am - 6:00pm</p>

      <div class="label-row label-where"><span class="lines"></span><span class="label">Where?</span><span class="lines"></span></div>
      <p class="event-address">4100 Linden Avenue<br>Suite 318 Rochester, NY 14618</p>

      <span class="marker marker-left"></span>
    </section>

    <div class="showroom-photo" role="img" aria-label="Showroom kitchen with white cabinets, granite island, pendant lights and red bar stools"></div>
    <span class="marker marker-right"></span>

    <div class="brand"><span class="brand-mark"></span><span class="brand-name">Cabinets by Hollowell</span></div>

    <section class="contact">
      <p class="contact-lead">Contact now for more information</p>
      <p class="contact-web">WWW.CABINETSBYHOLLOWELL.COM.</p>
      <p class="contact-phone">Call : 585.555.0142</p>
    </section>
  </main>
</body>
</html>
```